www.trelvonventuresgq.com

Design a professional Project Investor Pitch that give me the bestest and incredible WOW factor and its really Piques the INVESTER interest within first 2/3 slides of this businesse investor pitch

Target Market(s)

To reach INVESTORS that are Island minded and has knowledge of Philippines and want to see local economy grow and reduce foreign control of philippine islands and much more

Industry/Entity Type

Construction of Recycling Plant on Top 5 islands of the philippines

Font styles to use
Other font styles liked:
• Surprise me Designer :)

Colors

Designer to choose colors to be used in the design.

Requirements
Must have
• Plz check out my website and the attachments l sent .....its has to be be just like that pitch l sent to you but will need a updated version and the great WOW factor (just like in attachment 8) that wil grab Investors interest and keeness to be part of my projects company l have my origional pitch version and by all my create another one if u can do it better with the charts and bar graphs ...it must have exact same details on these charts/bar graphs in wording and details..it ya can create an amazing WOW factor investor pitch ...hit me with it !! Plz use the stats in the (Odari Investor Pitch) attachment 2 and input some bottling numbers as written but in charts/bar graphs format...
Nice to have
• just back yourself and give me the biggest WOW factor (like attachment 8) u can with exact same wording on the charts/bar graphs...just gimme best INVESTOR PiTCH ....think of this busines pitch as if your blood in your body absolutely depended on it !!!
Should not have
• Nothing misleading or illegal intent ....as this pitch is based on "Untapped Market" ..as its has Waste management but NO-ONE recyles the plastics / glasses/ cardboards etc ...Plz dont put in charts or bar graphs that are not true or illegal or misleading

```html
<!DOCTYPE html>
<html lang="en">
<head>
<meta charset="utf-8">
<title>Trelvon Ventures P/L – Investor Pitch</title>
<link href="https://fonts.googleapis.com/css2?family=Montserrat:wght@400;600;700;800&family=Poppins:wght@400;500;600;700&family=Josefin+Sans:wght@400;600&display=swap" rel="stylesheet">
<style>
:root{
  --page:#d6d7d9;
  --black:#000;
  --orange:#f7a21b;
  --white:#fff;
  --ink:#1c1c1c;
  --muted:#444;
  --blue:#2a8fd8;
  --red:#e3202a;
  --green:#2fae3f;
  --gold:#f4a11c;
  --navy:#0a3f8f;
  --mid-blue:#1a73b5;
  --sky:#2aa1e0;
  --panel:#f2f3f7;
  --table-bg:#f1f1f2;
  --vr-green:#2db13c;
  --thank-blue:#1e8fe0;
}
*{margin:0;padding:0;box-sizing:border-box}
html,body{width:1030px;height:1200px;overflow:hidden;background:var(--page)}
body{position:relative;font-family:'Poppins',sans-serif;color:var(--ink)}
.slide{position:absolute;width:452px;height:254px;overflow:hidden;background:var(--white)}
.s1{left:45px;top:56px;background:var(--black)}
.s2{left:522px;top:58px}
.s3{left:43px;top:331px}
.s4{left:520px;top:332px}
.s5{left:45px;top:613px}
.s6{left:523px;top:613px}
.s7{left:47px;top:890px}
.s8{left:523px;top:890px;background:#050505}

.header{position:absolute;left:0;top:0;width:100%;height:26px;background:var(--black);display:flex;align-items:center;padding-left:8px;z-index:2}
.brand-dot{width:12px;height:12px;border-radius:50%;background:var(--orange);flex:none}
.brand-name{font-family:'Montserrat',sans-serif;font-weight:700;color:var(--orange);font-size:8.5px;letter-spacing:3.4px;margin-left:12px;white-space:nowrap}
.header .divider{width:1px;height:14px;background:#666;margin:0 9px 0 7px}
.header .section{font-family:'Montserrat',sans-serif;font-weight:700;color:var(--orange);font-size:8.5px;white-space:nowrap}
.footer-tag{position:absolute;right:0;bottom:0;background:var(--black);color:var(--white);font-size:4.6px;padding:4px 7px;z-index:3}

/* cover */
.cover{position:absolute;inset:0;display:flex;flex-direction:column;align-items:center;text-align:center}
.cover .mark{width:40px;height:40px;border-radius:50%;background:var(--orange);margin-top:38px}
.cover .name{font-family:'Montserrat',sans-serif;font-weight:700;color:var(--orange);font-size:11px;letter-spacing:5.6px;margin-top:17px}
.cover .kicker{font-family:'Montserrat',sans-serif;font-weight:600;color:var(--white);font-size:14px;margin-top:20px}
.cover .title{font-family:'Montserrat',sans-serif;font-weight:800;color:var(--orange);font-size:16.5px;margin-top:5px}
.cover .sub{font-family:'Montserrat',sans-serif;color:var(--white);font-size:8.6px;margin-top:6px}
.cover .copy{font-family:'Montserrat',sans-serif;color:var(--white);font-size:7px;margin-top:28px}

/* agenda */
.photo{position:absolute}
.agenda-photo{left:0;top:26px;width:452px;height:228px;background:linear-gradient(115deg,#2a6b35 0%,#7fb389 22%,#e9eef0 42%,#cfd8dc 55%,#3b5a34 75%,#1f3a22 100%)}
.agenda{position:absolute;left:266px;top:63px;width:170px;display:flex;flex-direction:column;gap:4px}
.agenda li{list-style:none;background:rgba(150,150,150,.72);border:1px solid rgba(255,255,255,.25);color:#f4f4f4;font-size:7px;line-height:1.6;padding:4px 9px}

/* items */
.landfill-photo{left:0;top:26px;width:159px;height:228px;background:linear-gradient(180deg,#5d6e55 0%,#7e8b73 25%,#8a7b65 50%,#6b5d4c 75%,#9a9388 100%)}
.item{position:absolute;display:flex}
.item .icon{width:17px;height:17px;border-radius:50%;flex:none;display:flex;align-items:center;justify-content:center;margin-top:1px}
.item .icon svg{width:9px;height:9px}
.item h4{font-family:'Montserrat',sans-serif;font-weight:700;font-size:6.6px;color:var(--ink)}
.item p{font-size:5.2px;line-height:1.6;color:var(--muted);margin-top:3px}
.c-blue{background:var(--blue)}.c-red{background:var(--red)}.c-green{background:var(--green)}.c-gold{background:var(--gold)}

.focus-panel{position:absolute;left:230px;top:26px;width:222px;height:228px;background:var(--panel)}
.focus-title{position:absolute;left:246px;top:45px;font-family:'Josefin Sans',sans-serif;font-size:12.5px;color:#4f78b8;letter-spacing:.3px}
.focus-chart{position:absolute;left:230px;top:70px}
.bar-label{position:absolute;font-family:'Josefin Sans',sans-serif;font-size:5.6px;text-align:center;width:60px}
.bar-label b{display:block;color:#222;font-weight:600}
.bar-label span{color:#6b8fbf;line-height:1.3;display:block}

/* VR */
.pitch-label{position:absolute;left:12px;top:43px;font-family:'Montserrat',sans-serif;font-weight:700;font-size:6.5px}
.vr-table{position:absolute;left:12px;top:59px;width:245px;border-collapse:collapse;background:var(--table-bg);font-size:6.5px}
.vr-table td{height:19.4px;border-bottom:1px solid #d2d2d2;padding:0 0 0 13px}
.vr-table td.t{width:58px;padding-left:0}
.vr-total{position:absolute;left:12px;top:184px;width:245px;height:21px;background:var(--vr-green);color:var(--white);font-weight:700;font-size:6.6px;display:flex;align-items:center;justify-content:space-between;padding:0 42px 0 13px}
.cost-block{position:absolute;left:13px;top:216px;display:flex;align-items:center}
.cost-block .lbl{font-family:'Montserrat',sans-serif;font-weight:700}
.cost-block .lbl small{display:block;font-size:6.5px;color:var(--ink)}
.cost-block .lbl strong{display:block;font-size:11.5px;color:var(--vr-green);margin-top:1px}
.cost-block .sep{width:1px;height:24px;background:#bbb;margin:0 10px}
.cost-block .val small{display:block;font-family:'Montserrat',sans-serif;font-weight:700;font-size:6.6px}
.cost-block .val strong{display:block;font-family:'Montserrat',sans-serif;font-weight:800;font-size:11.5px;color:var(--vr-green);margin-top:1px}
.vr-photo-a{left:280px;top:31px;width:165px;height:115px;background:linear-gradient(160deg,#c9ced1 0%,#e8e6df 40%,#8c9498 75%,#5c6a6c 100%)}
.vr-photo-b{left:280px;top:153px;width:93px;height:94px;background:linear-gradient(170deg,#2b3e8f 0%,#4e5fa8 40%,#7a7f86 75%,#9a9ea3 100%)}
.vr-photo-c{left:379px;top:153px;width:66px;height:94px;background:linear-gradient(170deg,#8c8f93 0%,#c7c9cc 50%,#6e7175 100%)}

/* ROI */
.roi-bg{position:absolute;left:0;top:26px;width:452px;height:228px;background:linear-gradient(135deg,#3a1775 0%,#6a1d8f 35%,#a0248f 65%,#d83a77 100%)}
.roi-title{position:absolute;left:60px;top:38px;width:190px;text-align:center;font-family:'Montserrat',sans-serif;font-weight:800;font-size:13px;line-height:1.05;color:#b6a7ef}
.roi-chart{position:absolute;left:54px;top:74px;width:176px;height:170px;background:#f4f3f3;border-radius:3px}
.roi-legend{position:absolute;left:236px;top:111px;width:133px;height:133px;background:#f6f4f4;border-radius:3px;padding:12px 8px 0 9px}
.leg{display:flex;margin-bottom:9px}
.leg i{width:11px;height:11px;flex:none;margin-right:7px;margin-top:1px;border-radius:1px}
.leg b{display:block;font-family:'Montserrat',sans-serif;font-size:5.4px;color:#4a3aa8;font-weight:700}
.leg span{display:block;font-size:3.9px;line-height:1.25;color:#111;font-weight:600}

/* timeline */
.proj-badge{position:absolute;left:10px;top:42px;width:46px;height:44px;background:var(--black);display:flex;flex-direction:column;align-items:center;justify-content:center}
.proj-badge i{width:12px;height:12px;border-radius:50%;background:var(--orange)}
.proj-badge span{font-family:'Montserrat',sans-serif;font-weight:700;font-size:3.2px;color:var(--orange);letter-spacing:.6px;margin-top:3px;text-align:center;line-height:1.3}
.proj-title{position:absolute;left:62px;top:44px;font-family:'Montserrat',sans-serif;font-weight:700;font-size:13px;color:#233066}
.proj-meta{position:absolute;left:63px;top:62px;font-family:'Montserrat',sans-serif;font-size:7.8px;color:#2a86d8;line-height:1.35;display:grid;grid-template-columns:79px auto}
.milestones{position:absolute;left:10px;top:95px}
.notes{position:absolute;left:209px;top:88px;width:97px}
.note{border-bottom:1px dotted #bbb;padding-bottom:3px;margin-bottom:4px}
.note:last-child{border:0}
.note h5{font-family:'Montserrat',sans-serif;font-weight:700;font-size:5.4px}
.note p{font-size:3.8px;line-height:1.35;font-weight:600;margin-top:2px;color:#222}
.n1 h5{color:#27a3b3}.n2 h5{color:#ef4a2f}.n3 h5{color:#d1571c}.n4 h5{color:#2a78c8}
.proj-heading{position:absolute;left:319px;top:103px;font-family:'Montserrat',sans-serif;font-weight:800;font-size:12.6px;line-height:1.45;color:#111;white-space:nowrap}
.proj-heading span{display:block}

/* thank you */
.thanks-bg{position:absolute;inset:0;background:radial-gradient(circle at 38% 45%,#141414 0%,#050505 70%)}
.thanks-mark{position:absolute;left:98px;top:89px;width:40px;height:40px;border-radius:50%;background:var(--orange)}
.thanks-name{position:absolute;left:35px;top:137px;font-family:'Montserrat',sans-serif;font-weight:700;color:var(--orange);font-size:8.6px;letter-spacing:4.2px}
.thanks-sep{position:absolute;left:219px;top:69px;width:1px;height:95px;background:#3a3a3a}
.thanks-word{position:absolute;left:244px;top:101px;font-family:'Montserrat',sans-serif;font-weight:800;font-size:29px;color:var(--thank-blue)}
</style>
</head>
<body>

<section class="slide s1">
  <div class="cover">
    <div class="mark"></div>
    <div class="name">TRELVON VENTURES P/L</div>
    <div class="kicker">INVESTOR PITCH</div>
    <div class="title">RECYCLING PLANT PHILIPPINES</div>
    <div class="sub">Investment opportunity in sustainable recycling solutions</div>
    <div class="copy">Trelvon Ventures P/L 2026 ©</div>
  </div>
</section>

<section class="slide s2">
  <header class="header"><span class="brand-dot"></span><span class="brand-name">TRELVON VENTURES P/L</span><span class="divider"></span><span class="section">PRESENTATION AGENDA</span></header>
  <div class="photo agenda-photo" role="img" aria-label="Person holding a white recycling bin filled with plastic bottles"></div>
  <ul class="agenda">
    <li>Overview of the Recycling Industry in the Philippines</li>
    <li>Business Model and Value Proposition</li>
    <li>Operational Plan and Technology</li>
    <li>Financial Projections and Investment Opportunity</li>
    <li>Environmental and Social Impact</li>
  </ul>
  <div class="footer-tag">Trelvon Ventures P/L 2026 ©</div>
</section>

<section class="slide s3">
  <header class="header"><span class="brand-dot"></span><span class="brand-name">TRELVON VENTURES P/L</span><span class="divider"></span><span class="section">CURRENT WASTE MANAGEMENT LANDSCAPE</span></header>
  <div class="photo landfill-photo" role="img" aria-label="Worker sorting plastic waste at an open dump site"></div>
  <div class="item" style="left:175px;top:44px;width:265px"><span class="icon c-blue"><svg viewBox="0 0 10 10"><path d="M3 1h4l-1 8H4z" fill="#fff"/></svg></span><div style="margin-left:25px"><h4>PLASTIC WASTE GENERATION</h4><p>On Boracay Island produces about 36,500 tons of plastic waste annually, impacting ocean pollution significantly and that's just 1 island out of 7700+ islands of Philippines</p></div></div>
  <div class="item" style="left:175px;top:98px;width:265px"><span class="icon c-red"><svg viewBox="0 0 10 10"><rect x="2.5" y="3" width="5" height="6" fill="#fff"/><rect x="2" y="1.5" width="6" height="1" fill="#fff"/></svg></span><div style="margin-left:25px"><h4>WASTE COLLECTION CHALLENGES</h4><p>Of the 100 tons of Plastic Waste per day ...Only 40-50% of waste is effectively collected, with much ending up in open dumps or oceans and its causing environmental harm daily</p></div></div>
  <div class="item" style="left:175px;top:154px;width:265px"><span class="icon c-green"><svg viewBox="0 0 10 10"><path d="M5 1l2 3H3zM1.5 8l2-3 1.5 3zM8.5 8H6l1.5-3z" fill="#fff"/></svg></span><div style="margin-left:25px"><h4>ROLE OF INFORMAL RECYCLING</h4><p>Informal recycling contributes significantly but remains unstructured and inconsistent across regions in the Philippines.</p></div></div>
  <div class="item" style="left:175px;top:201px;width:265px"><span class="icon c-gold"><svg viewBox="0 0 10 10"><rect x="2.5" y="2" width="5" height="7" rx="1" fill="#fff"/></svg></span><div style="margin-left:25px"><h4>WASTE SEGREGATION EFFORTS</h4><p>Efforts to improve waste segregation at the source exist but are inconsistent and vary widely by region.</p></div></div>
  <div class="footer-tag">Trelvon Ventures P/L 2026 ©</div>
</section>

<section class="slide s4">
  <header class="header"><span class="brand-dot"></span><span class="brand-name">TRELVON VENTURES P/L</span><span class="divider"></span><span class="section">MARKET DEMAND FOR RECYCLING SERVICES</span></header>
  <div class="item" style="left:12px;top:44px;width:200px"><span class="icon c-blue" style="width:31px;height:31px"><svg viewBox="0 0 10 10" style="width:14px;height:14px"><path d="M5 1l2 3H3zM1.5 8l2-3 1.5 3zM8.5 8H6l1.5-3z" fill="#fff"/></svg></span><div style="margin-left:10px"><h4>RISING RECYCLING AWARENESS</h4><p>Increased public awareness and government campaigns boost demand for recycling services in the Philippines.</p></div></div>
  <div class="item" style="left:12px;top:94px;width:200px"><span class="icon c-red" style="width:31px;height:31px"><svg viewBox="0 0 10 10" style="width:14px;height:14px"><circle cx="5" cy="5" r="3" fill="none" stroke="#fff" stroke-width="1.2"/><rect x="4" y="4" width="2" height="2" fill="#fff"/></svg></span><div style="margin-left:10px"><h4>INDUSTRY GROWTH VALUE</h4><p>The recycling industry in the Philippines is valued in hundreds of millions USD, showing steady annual growth.</p></div></div>
  <div class="item" style="left:12px;top:144px;width:200px"><span class="icon c-green" style="width:31px;height:31px"><svg viewBox="0 0 10 10" style="width:14px;height:14px"><circle cx="5" cy="5" r="3.5" fill="none" stroke="#fff" stroke-width="1"/><path d="M1.5 5h7M5 1.5v7" stroke="#fff" stroke-width=".8"/></svg></span><div style="margin-left:10px"><h4>DRIVERS OF EXPANSION</h4><p>Urbanization, consumerism, and environmental advocacy propel expansion opportunities in recycling services.</p></div></div>
  <div class="item" style="left:12px;top:196px;width:200px"><span class="icon c-gold" style="width:31px;height:31px"><svg viewBox="0 0 10 10" style="width:14px;height:14px"><path d="M1 5l2-2 2 1 2-1 2 2-3 3z" fill="#fff"/></svg></span><div style="margin-left:10px"><h4>COLLABORATIVE EFFORTS</h4><p>Businesses and municipalities seek partnerships for responsible waste disposal and circular economy efforts.</p></div></div>
  <div class="focus-panel"></div>
  <div class="focus-title">Recycling Plant Focus</div>
  <svg class="focus-chart" width="222" height="112" viewBox="0 0 222 112">
    <g stroke="#dfe1e6" stroke-width=".5">
      <line x1="20" y1="12" x2="218" y2="12"/><line x1="20" y1="20" x2="218" y2="20"/><line x1="20" y1="30" x2="218" y2="30"/><line x1="20" y1="40" x2="218" y2="40"/><line x1="20" y1="55" x2="218" y2="55"/><line x1="20" y1="67" x2="218" y2="67"/><line x1="20" y1="77" x2="218" y2="77"/><line x1="20" y1="87" x2="218" y2="87"/>
    </g>
    <line x1="20" y1="4" x2="20" y2="107" stroke="#333" stroke-width=".6"/>
    <line x1="20" y1="107" x2="218" y2="107" stroke="#2a5aa8" stroke-width=".8"/>
    <g font-family="Poppins,sans-serif" font-size="3.6" fill="#333"><text x="6" y="32">60%</text><text x="6" y="78">35%</text><text x="7" y="102">5%</text></g>
    <rect x="20" y="29" width="41" height="78" fill="var(--navy)"/>
    <rect x="76" y="77" width="40" height="30" fill="var(--mid-blue)"/>
    <rect x="131" y="97" width="40" height="10" fill="var(--sky)"/>
  </svg>
  <div class="bar-label" style="left:241px;top:190px"><b>Plastics 60%</b><span>Production Turnover</span></div>
  <div class="bar-label" style="left:295px;top:190px"><b>Glass 35%</b><span>Production Turnover</span></div>
  <div class="bar-label" style="left:356px;top:190px;width:70px"><b>Paper / Cardboard&nbsp; 5%</b><span>Production Turnover</span></div>
  <div class="footer-tag">Trelvon Ventures P/L 2026 ©</div>
</section>

<section class="slide s5">
  <header class="header"><span class="brand-dot"></span><span class="brand-name">TRELVON VENTURES P/L</span><span class="divider"></span><span class="section">VIRTUAL REALITY &nbsp;(HEADSET / PC PRESENTATION</span></header>
  <div class="pitch-label">PRIMARY INVESTOR PITCH :</div>
  <table class="vr-table">
    <tr><td>Seeing landsite during demolition</td><td class="t">30 secs</td></tr>
    <tr><td>Seeing Development of Recycling plant</td><td class="t">1 mins</td></tr>
    <tr><td>Seeing Garbage trucks enter and dumping</td><td class="t">30 secs</td></tr>
    <tr><td>Seeing Recycling &amp; Labelling of Plastic bottles</td><td class="t">1 mins</td></tr>
    <tr><td>Seeing Logistics Trucks with Bottles</td><td class="t">1 mins</td></tr>
    <tr><td>Seeing Distribution of Bottles to Shops/Resorts</td><td class="t">1 mins</td></tr>
  </table>
  <div class="vr-total"><span>Total &nbsp;VR Format</span><span>5 Mins</span></div>
  <div class="cost-block">
    <div class="lbl"><small>DURATION</small><strong>COSTS</strong></div>
    <span class="sep"></span>
    <div class="val"><small>6 WEEKS / EDITING / RECORDING/ VOICEOVER/ AI</small><strong>$35,000 AUD</strong></div>
  </div>
  <div class="photo vr-photo-a" role="img" aria-label="Person wearing a VR headset in an office"></div>
  <div class="photo vr-photo-b" role="img" aria-label="Virtual warehouse scene with a presenter avatar"></div>
  <div class="photo vr-photo-c" role="img" aria-label="VR headset and controllers"></div>
  <div class="footer-tag">Trelvon Ventures P/L 2026 ©</div>
</section>

<section class="slide s6">
  <header class="header"><span class="brand-dot"></span><span class="brand-name">TRELVON VENTURES P/L</span></header>
  <div class="roi-bg"></div>
  <div class="roi-title">RETURN ON INVESTMENT &amp; EXIT STRATEGIES</div>
  <div class="roi-chart">
    <svg width="176" height="170" viewBox="0 0 176 170">
      <g stroke="#b8b8b8" stroke-width=".5" stroke-dasharray="2 2">
        <line x1="27" y1="31" x2="165" y2="31"/><line x1="27" y1="47" x2="165" y2="47"/><line x1="27" y1="64" x2="165" y2="64"/><line x1="27" y1="80" x2="165" y2="80"/><line x1="27" y1="97" x2="165" y2="97"/><line x1="27" y1="113" x2="165" y2="113"/><line x1="27" y1="130" x2="165" y2="130"/><line x1="27" y1="146" x2="165" y2="146"/>
      </g>
      <line x1="27" y1="10" x2="27" y2="156" stroke="#555" stroke-width=".6"/>
      <line x1="27" y1="156" x2="165" y2="156" stroke="#555" stroke-width=".6"/>
      <g font-family="Poppins,sans-serif" font-size="5" fill="#333">
        <text x="10" y="13">%</text><text x="8" y="33">100</text><text x="10" y="50">80</text><text x="10" y="83">60</text><text x="10" y="116">40</text><text x="10" y="149">20</text>
      </g>
      <rect x="36" y="32" width="12" height="124" fill="#e23c3c"/>
      <rect x="66" y="83" width="12" height="73" fill="#6ed07a"/>
      <rect x="97" y="99" width="11" height="57" fill="#c49be8"/>
    </svg>
  </div>
  <div class="roi-legend">
    <div class="leg"><i style="background:#e23c3c"></i><div><b>Expected ROI Timeline</b><span>Return on Invesment expected to be achieved by year 5-7 &amp; even more achievable in less time via private investing influened by market &amp; operational efficiency</span></div></div>
    <div class="leg"><i style="background:#6ed07a"></i><div><b>Exit Strategies &nbsp;/ &nbsp;Options</b><span>Exit Strategies inclues Sales to Waste Management firms &amp; Acquisition by sustainibility investors</span></div></div>
    <div class="leg"><i style="background:#c49be8"></i><div><b>ESG Alignment</b><span>Project aligns with ESG Criteria, making it attractive to impact Investors focused on sustainability &amp; financial returns</span></div></div>
  </div>
  <div class="footer-tag">Trelvon Ventures P/L 2026 ©</div>
</section>

<section class="slide s7">
  <header class="header"><span class="brand-dot"></span><span class="brand-name">TRELVON VENTURES P/L</span></header>
  <div class="proj-badge"><i></i><span>TRELVON<br>VENTURES<br>P/L</span></div>
  <div class="proj-title">Boracay Recycling Plant 2026</div>
  <div class="proj-meta"><span>Project Lead:</span><span>Rowan Keele</span><span>Assigned Team:</span><span>Trelvon Ventures P/L Team</span></div>
  <svg class="milestones" width="196" height="150" viewBox="0 0 196 150">
    <g font-family="Montserrat,sans-serif" font-weight="600" font-size="7">
      <text x="2" y="71" fill="#3aa4b3">8-10 mths</text>
      <text x="52" y="54" fill="#6bc24a">Year 2</text>
      <text x="90" y="38" fill="#2a9ec7">Year 3-6</text>
      <text x="142" y="8" fill="#2a78c8">Year 5-7</text>
    </g>
    <path d="M24 77l-5 6h3v8h4v-8h3z" fill="#3aa4b3"/>
    <path d="M70 60l-5 6h3v8h4v-8h3z" fill="#6bc24a"/>
    <path d="M113 43l-5 6h3v8h4v-8h3z" fill="#2a9ec7"/>
    <path d="M161 13l-5 6h3v8h4v-8h3z" fill="#2a78c8"/>
    <path d="M12 99l5-6h24l5 6z" fill="#3aa4b3"/><rect x="12" y="99" width="34" height="45" fill="#5cc9c2"/><rect x="18" y="99" width="22" height="45" fill="#7fe0d8"/>
    <path d="M55 81l5-6h20l5 6z" fill="#4fb03a"/><rect x="55" y="81" width="30" height="63" fill="#6fd34a"/><rect x="60" y="81" width="20" height="63" fill="#8ae65f"/>
    <path d="M97 64l6-8h23l6 8z" fill="#2a9ec7"/><rect x="97" y="64" width="35" height="80" fill="#b04a1a"/><rect x="103" y="64" width="23" height="80" fill="#c75a24"/>
    <path d="M144 31l6-8h28l6 8z" fill="#1d6fc7"/><rect x="144" y="31" width="40" height="113" fill="#1d62b8"/><rect x="151" y="31" width="26" height="113" fill="#2d82d6"/>
    <line x1="0" y1="144" x2="196" y2="144" stroke="#ccc" stroke-width=".6"/>
  </svg>
  <div class="notes">
    <div class="note n1"><h5>REVENUE GENERATION START</h5><p>Revenue is expected to begin in the 8-10th month after construction of recycling plant &amp; Marking the start of Income flow</p></div>
    <div class="note n2"><h5>BREAK-EVEN FORECAST</h5><p>Break-even is projected by the end of Year 2 by balancing cost &amp; revenue effectively</p></div>
    <div class="note n3"><h5>Profit Margin Growth</h5><p>Profits are expected to grow 20-25% by year 3 per island recycling plant &amp; growing soft drink refilling distribution by 40-50% by year 6 due to operational effiiciencies &amp; scaling</p></div>
    <div class="note n4"><h5>Cash Flow &amp; Sensitivity</h5><p>Strong cash flow with liquidity post break-even considering sensivitiy to market demand and collection rates</p></div>
  </div>
  <h2 class="proj-heading"><span>PROJECTED</span><span>REVENUE AND</span><span>PROFITABILITY</span><span>TIMELINES</span></h2>
  <div class="footer-tag">Trelvon Ventures P/L 2026 ©</div>
</section>

<section class="slide s8">
  <div class="thanks-bg"></div>
  <div class="thanks-mark"></div>
  <div class="thanks-name">TRELVON VENTURES P/L</div>
  <div class="thanks-sep"></div>
  <div class="thanks-word">THANK YOU</div>
</section>

</body>
</html>
```